Business Card design for construction company

I would like a business card design for a construction company - Harlow Constructions. I have attached the ai logo file for use. I would like the card to be very smart and clean and incorporate only white and the two colours in the logo. I would like the card to have two sides. One side can just have the logo, the other with the relevant information.

Target Market(s)

Building and Construction Clients

Industry/Entity Type

Business

Contact Information for Business Card

Name: Tom Pardoe
Company: Harlow Constructions Pty Limited
Address: 14 Mallee Crescent Carrow Vale 2093
Phone: 0427 531 068
Email: tomp@harlowbuild-example.com.au

Font styles to use
Serif
Sans Serif

Requirements
Must have
• Details noted above
• Logo as provided
• Colours as in logo
• Square edges
• A font that compliments the logo
Should not have
• Any colour other than white and those in logo
• Rounded edges

```html
<!DOCTYPE html>
<html lang="en">
<head>
<meta charset="utf-8">
<title>Harlow Constructions – Business Card</title>
<link rel="stylesheet" href="https://fonts.googleapis.com/css2?family=Didact+Gothic&display=swap">
<style>
  :root {
    --backdrop: #2f3c43;
    --card-white: #ffffff;
    --band-grey: #58595b;
    --logo-grey: #4d4d4f;
    --accent-blue: #3fa9dc;
    --text-white: #ffffff;
  }
  * { box-sizing: border-box; margin: 0; padding: 0; }
  html, body {
    width: 1200px;
    height: 900px;
    overflow: hidden;
    background: var(--backdrop);
    font-family: "Didact Gothic", "Helvetica Neue", Arial, sans-serif;
  }
  .canvas {
    position: relative;
    width: 1200px;
    height: 900px;
  }
  .card {
    position: absolute;
    left: 290px;
    width: 620px;
    height: 378px;
    background: var(--card-white);
  }
  .card--front { top: 52px; }
  .card--back { top: 470px; }

  .band {
    position: absolute;
    left: 0;
    width: 100%;
    background: var(--band-grey);
  }
  .card--front .band {
    top: 129px;
    height: 102px;
    display: flex;
    align-items: center;
    justify-content: center;
  }
  .card--back .band {
    top: 193px;
    height: 92px;
    display: flex;
    align-items: center;
  }

  .wordmark {
    font-size: 22px;
    letter-spacing: 0.16em;
    text-transform: uppercase;
    white-space: nowrap;
  }
  .card--front .wordmark { color: var(--text-white); }
  .card--back .wordmark {
    position: absolute;
    top: 108px;
    left: 0;
    width: 100%;
    text-align: center;
    color: var(--logo-grey);
  }

  .person {
    width: 230px;
    padding-right: 24px;
    text-align: right;
  }
  .person__name {
    display: block;
    color: var(--text-white);
    font-size: 24px;
    font-variant: small-caps;
    letter-spacing: 0.08em;
    line-height: 1.1;
  }
  .person__role {
    display: block;
    color: var(--accent-blue);
    font-size: 11px;
    letter-spacing: 0.14em;
    text-transform: uppercase;
    margin-top: 2px;
  }

  .contact {
    list-style: none;
    padding-left: 30px;
  }
  .contact__item {
    color: var(--text-white);
    font-size: 13px;
    font-variant: small-caps;
    letter-spacing: 0.06em;
    line-height: 22px;
    white-space: nowrap;
  }
  .contact__label { color: var(--accent-blue); }
</style>
</head>
<body>
  <main class="canvas">
    <section class="card card--front" aria-label="Business card, logo side">
      <div class="band">
        <span class="wordmark">Harlow Constructions</span>
      </div>
    </section>

    <section class="card card--back" aria-label="Business card, details side">
      <span class="wordmark">Harlow Constructions</span>
      <div class="band">
        <div class="person">
          <span class="person__name">Tom Pardoe</span>
          <span class="person__role">Director</span>
        </div>
        <ul class="contact">
          <li class="contact__item"><span class="contact__label">Address:</span> 14 Mallee Crescent Carrow Vale 2093</li>
          <li class="contact__item"><span class="contact__label">Phone:</span> 0427 531 068</li>
          <li class="contact__item"><span class="contact__label">Email:</span> tomp@harlowbuild-example.com.au</li>
        </ul>
      </div>
    </section>
  </main>
</body>
</html>
```